Social Action Network Needs Banner Ads for Cause T-Shirts

Hope in Hand is a social action network that transforms ordinary internet actions into donations to non-profit organizations fighting for a better tomorrow. Users can donate their social influence, print coupons, accept free offers or shop online and every action benefits causes they love. You can watch a video here: http://www.hopeinhand.example/

We are about to launch a line of cause tees that benefit the various causes we support. We want the banner ads to be positive, uplifting, inspiring and attractive. We want the ads to incorporate the following wording (although, we encourage creativity): Dress better so others can live better.

We require typical banner ad sizes: 300 x 250, 160 x 600, 728 x 90 (more sizes would be much appreciated).

Please try to include the Hope in Hand logo (color can be changed based on ad design).

In case it helps, here is a link to a page we have set up for one of our partner charities: http://www.hopeinhand.example/KindnessWells

Target Market(s)

While 80% of our users are women, we need to appeal to both.

Industry/Entity Type

Non-Profit

Requirements
Must have
• Hope in Hand logo and T-shirt design (with or without model). Also, some sort of call to action button - get tees, take action, buy now, check it out, learn more, etc.
Nice to have
• Feature the woman's tees and if possible the man's tees could be somewhere smaller in the background (if design allows).

```html
<!DOCTYPE html>
<html lang="en">
<head>
<meta charset="utf-8">
<title>Hope in Hand – Cause Tee Banner Set</title>
<link rel="stylesheet" href="https://fonts.googleapis.com/css2?family=Bebas+Neue&family=Crimson+Text&display=swap">
<style>
  :root {
    --stage-light: #f2f2f2;
    --stage-dark: #d6d6d6;
    --sun: #f7c600;
    --lime: #b7d11e;
    --leaf: #5cb93a;
    --forest: #17a05a;
    --olive: #a9a100;
    --cream: #eef6cf;
    --white: #ffffff;
    --ink: #222222;
    --btn-top: #2f7fd0;
    --btn-mid: #0e4f93;
    --btn-bottom: #062c5a;
    --shirt-blue: #1e8fd6;
    --shirt-grey: #4b4f52;
    --logo-red: #d81f26;
  }
  * { box-sizing: border-box; margin: 0; padding: 0; }
  html, body { width: 1200px; height: 808px; overflow: hidden; }
  body {
    position: relative;
    background: radial-gradient(ellipse at 40% 20%, var(--stage-light) 0%, var(--stage-dark) 100%);
    font-family: "Bebas Neue", "Arial Narrow", sans-serif;
  }

  .ad-slot { position: absolute; box-shadow: 2px 3px 6px rgba(0,0,0,.35); border: 1px solid #111; overflow: hidden; }
  .ad { position: absolute; left: 0; top: 0; transform-origin: 0 0; transform: scale(var(--s)); overflow: hidden;
        background: linear-gradient(160deg, var(--sun) 0%, var(--lime) 40%, var(--leaf) 68%, var(--forest) 100%); }

  .photo { position: absolute; }
  .photo-woman { background: linear-gradient(180deg, #6b4a3a 0%, #8a6a55 22%, var(--shirt-blue) 30%, #1676b8 80%, #1a1a1a 100%); border-radius: 30px 30px 0 0; }
  .photo-man { background: linear-gradient(180deg, #5a3e30 0%, #b98f76 25%, var(--shirt-grey) 40%, #3a3d40 100%); border-radius: 20px 20px 0 0; }

  .headline-box { position: absolute; background: var(--white); color: var(--olive); }
  .headline-box span, .tagline span { display: block; }
  .tagline { position: absolute; color: var(--cream); text-align: right; }

  .cta { position: absolute; display: flex; align-items: center; justify-content: center; gap: .4em;
         color: var(--white); border-radius: 9px;
         background: linear-gradient(180deg, var(--btn-top) 0%, var(--btn-mid) 45%, var(--btn-bottom) 100%);
         box-shadow: 0 2px 4px rgba(0,0,0,.45); letter-spacing: .5px; }
  .cta svg { fill: var(--white); }

  .brand { position: absolute; display: flex; align-items: center; }
  .brand-mark { border-radius: 50%; background: var(--white); border: 2px solid var(--ink); flex: none; }
  .brand-name { font-family: "Crimson Text", Georgia, serif; color: var(--ink); white-space: nowrap; }

  .swoosh { position: absolute; left: 0; bottom: 0; }
  .white-band { position: absolute; background: var(--white); }

  /* 300 x 250 base */
  .ad-medium { width: 300px; height: 250px; }
  .ad-medium .photo-woman { left: 198px; top: 2px; width: 102px; height: 168px; }
  .ad-medium .photo-man { left: 2px; top: 84px; width: 48px; height: 110px; }
  .ad-medium .headline-box { left: 43px; top: 2px; width: 95px; height: 67px; padding: 2px 0 0 5px; font-size: 35px; line-height: 31px; }
  .ad-medium .tagline { left: 48px; top: 71px; width: 130px; font-size: 37px; line-height: 33px; }
  .ad-medium .cta { left: 120px; top: 177px; width: 168px; height: 38px; font-size: 29px; }
  .ad-medium .brand { left: 9px; top: 203px; gap: 5px; }
  .ad-medium .brand-mark { width: 37px; height: 37px; }
  .ad-medium .brand-name { font-size: 16px; }

  /* 160 x 600 base */
  .ad-sky { width: 160px; height: 600px; }
  .ad-sky .photo-woman { left: 45px; top: 6px; width: 110px; height: 211px; }
  .ad-sky .white-band { left: 0; width: 160px; }
  .ad-sky .headline-box { left: 0; top: 217px; width: 160px; height: 61px; padding: 2px 0 0 20px; font-size: 34px; line-height: 29px; }
  .ad-sky .tagline { left: 0; top: 280px; width: 146px; font-size: 35px; line-height: 31px; }
  .ad-sky .cta { left: 18px; top: 380px; width: 130px; height: 32px; font-size: 23px; }
  .ad-sky .photo-man { left: 40px; top: 420px; width: 80px; height: 121px; }
  .ad-sky .brand { left: 10px; top: 548px; gap: 6px; }
  .ad-sky .brand-mark { width: 40px; height: 40px; }
  .ad-sky .brand-name { font-size: 18px; }

  /* 468 x 60 base */
  .ad-banner { width: 468px; height: 60px; }
  .ad-banner .photo-woman { left: 10px; top: 0; width: 140px; height: 60px; border-radius: 0; }
  .ad-banner .headline-box { left: 149px; top: 0; width: 72px; height: 60px; padding: 5px 0 0 5px; font-size: 24px; line-height: 22px; }
  .ad-banner .tagline { left: 222px; top: 2px; width: 78px; font-size: 19px; line-height: 18px; }
  .ad-banner .photo-man { left: 306px; top: 4px; width: 44px; height: 56px; }
  .ad-banner .brand { left: 362px; top: 3px; gap: 4px; }
  .ad-banner .brand-mark { width: 22px; height: 22px; border-width: 1px; }
  .ad-banner .brand-name { font-size: 10px; }
  .ad-banner .cta { left: 356px; top: 30px; width: 104px; height: 23px; font-size: 16px; border-radius: 6px; }

  /* 728 x 90 base */
  .ad-leader { width: 728px; height: 90px; }
  .ad-leader .photo-man.first { left: 2px; top: 4px; width: 78px; height: 86px; }
  .ad-leader .photo-woman { left: 110px; top: 0; width: 140px; height: 90px; border-radius: 0; }
  .ad-leader .headline-box { left: 252px; top: 0; width: 101px; height: 90px; padding: 10px 0 0 8px; font-size: 40px; line-height: 34px; }
  .ad-leader .tagline { left: 358px; top: 4px; width: 108px; font-size: 30px; line-height: 27px; }
  .ad-leader .photo-man.second { left: 472px; top: 6px; width: 62px; height: 84px; }
  .ad-leader .brand { left: 556px; top: 3px; gap: 6px; }
  .ad-leader .brand-mark { width: 38px; height: 38px; }
  .ad-leader .brand-name { font-size: 19px; }
  .ad-leader .cta { left: 553px; top: 49px; width: 144px; height: 34px; font-size: 27px; }
</style>
</head>
<body>

<!-- 300x250 small -->
<div class="ad-slot" style="left:698px; top:52px; width:197px; height:165px;">
  <div class="ad ad-medium" style="--s:0.657;">
    <div class="photo photo-woman" role="img" aria-label="Model wearing the blue women's cause tee"></div>
    <div class="photo photo-man" role="img" aria-label="Model wearing the grey men's cause tee"></div>
    <div class="headline-box"><span>Dress</span><span>Better</span></div>
    <div class="tagline"><span>So others</span><span>can live</span><span>better.</span></div>
    <svg class="swoosh" width="300" height="70" viewBox="0 180 300 70"><path d="M0 192 C110 186 215 205 275 250 L0 250 Z" fill="#ffffff"/></svg>
    <div class="brand"><span class="brand-mark"></span><span class="brand-name">Hope in Hand</span></div>
    <div class="cta">Get Tees <svg width="14" height="16" viewBox="0 0 14 16"><path d="M0 0 L14 8 L0 16 Z"/></svg></div>
  </div>
</div>

<!-- 300x250 -->
<div class="ad-slot" style="left:169px; top:274px; width:329px; height:274px;">
  <div class="ad ad-medium" style="--s:1.097;">
    <div class="photo photo-woman" role="img" aria-label="Model wearing the blue women's cause tee"></div>
    <div class="photo photo-man" role="img" aria-label="Model wearing the grey men's cause tee"></div>
    <div class="headline-box"><span>Dress</span><span>Better</span></div>
    <div class="tagline"><span>So others</span><span>can live</span><span>better.</span></div>
    <svg class="swoosh" width="300" height="70" viewBox="0 180 300 70"><path d="M0 192 C110 186 215 205 275 250 L0 250 Z" fill="#ffffff"/></svg>
    <div class="brand"><span class="brand-mark"></span><span class="brand-name">Hope in Hand</span></div>
    <div class="cta">Get Tees <svg width="14" height="16" viewBox="0 0 14 16"><path d="M0 0 L14 8 L0 16 Z"/></svg></div>
  </div>
</div>

<!-- 336x280 -->
<div class="ad-slot" style="left:526px; top:241px; width:368px; height:306px;">
  <div class="ad ad-medium" style="--s:1.226;">
    <div class="photo photo-woman" role="img" aria-label="Model wearing the blue women's cause tee"></div>
    <div class="photo photo-man" role="img" aria-label="Model wearing the grey men's cause tee"></div>
    <div class="headline-box"><span>Dress</span><span>Better</span></div>
    <div class="tagline"><span>So others</span><span>can live</span><span>better.</span></div>
    <svg class="swoosh" width="300" height="70" viewBox="0 180 300 70"><path d="M0 192 C110 186 215 205 275 250 L0 250 Z" fill="#ffffff"/></svg>
    <div class="brand"><span class="brand-mark"></span><span class="brand-name">Hope in Hand</span></div>
    <div class="cta">Get Tees <svg width="14" height="16" viewBox="0 0 14 16"><path d="M0 0 L14 8 L0 16 Z"/></svg></div>
  </div>
</div>

<!-- 160x600 -->
<div class="ad-slot" style="left:930px; top:99px; width:177px; height:655px;">
  <div class="ad ad-sky" style="--s:1.09;">
    <div class="photo photo-woman" role="img" aria-label="Model wearing the blue women's cause tee"></div>
    <div class="headline-box"><span>Dress</span><span>Better</span></div>
    <div class="tagline"><span>So others</span><span>can live</span><span>better.</span></div>
    <div class="cta">Get Tees <svg width="11" height="13" viewBox="0 0 14 16"><path d="M0 0 L14 8 L0 16 Z"/></svg></div>
    <div class="photo photo-man" role="img" aria-label="Model wearing the grey men's cause tee"></div>
    <div class="white-band" style="top:541px; height:59px;"></div>
    <div class="brand"><span class="brand-mark"></span><span class="brand-name">Hope in Hand</span></div>
  </div>
</div>

<!-- 468x60 -->
<div class="ad-slot" style="left:383px; top:568px; width:512px; height:68px;">
  <div class="ad ad-banner" style="--s:1.094;">
    <div class="photo photo-woman" role="img" aria-label="Close-up of the blue women's cause tee"></div>
    <div class="headline-box"><span>Dress</span><span>Better</span></div>
    <div class="tagline"><span>So others</span><span>can live</span><span>better.</span></div>
    <div class="photo photo-man" role="img" aria-label="Model wearing the grey men's cause tee"></div>
    <div class="brand"><span class="brand-mark"></span><span class="brand-name">Hope in Hand</span></div>
    <div class="cta">Get Tees <svg width="8" height="9" viewBox="0 0 14 16"><path d="M0 0 L14 8 L0 16 Z"/></svg></div>
  </div>
</div>

<!-- 728x90 -->
<div class="ad-slot" style="left:99px; top:655px; width:796px; height:99px;">
  <div class="ad ad-leader" style="--s:1.094;">
    <div class="photo photo-man first" role="img" aria-label="Model wearing the grey men's cause tee"></div>
    <div class="photo photo-woman" role="img" aria-label="Close-up of the blue women's cause tee"></div>
    <div class="headline-box"><span>Dress</span><span>Better</span></div>
    <div class="tagline"><span>So others</span><span>can live</span><span>better.</span></div>
    <div class="photo photo-man second" role="img" aria-label="Model wearing the grey men's cause tee"></div>
    <div class="brand"><span class="brand-mark"></span><span class="brand-name">Hope in Hand</span></div>
    <div class="cta">Get Tees <svg width="12" height="14" viewBox="0 0 14 16"><path d="M0 0 L14 8 L0 16 Z"/></svg></div>
  </div>
</div>

</body>
</html>
```